Marwell Herd Services concrete grooving services flyer design

Marwell Herd Services offers 4 different grooving options:

DEEP GROOVING
, ideal for Safety & Efficiency
Our hugely popular deep straight line grooving, long lasting, minimal hoof wear,

Create safe and secure flooring, cows walk without hesitation

Achieve groove spacing for optimal hoof function, reduce hoof trauma

Ideal grooves to new concrete or surfaces with little to no pattern or previous grooving

Ideal groove pattern as promoted by The pasturewide programme

MINI GROOVING,
Smaller dimensions Ideal option for heifer housing and high activity areas such as parlours and handling areas

An ideal solution for regaining traction on old previous grooving that has lost its traction without loosing stability

Plaining

smoothing down rough concrete with previous aggressive grooving or patterns to reduce hoof trauma & wear

SENSOR PLATE SINKING

sinking sensor plates for automated machines below surface level preventing accidental damage & wear

```html
<!DOCTYPE html>
<html lang="en">
<head>
<meta charset="utf-8">
<title>Marwell Herd Services – Concrete Grooving</title>
<link rel="stylesheet" href="https://fonts.googleapis.com/css2?family=Ubuntu:wght@300;400&display=swap">
<style>
  :root {
    --olive-dark: #6f6208;
    --olive: #a8940f;
    --gold: #e0b800;
    --yellow: #ffd900;
    --lime: #9ad600;
    --forest: #3f6410;
    --mint: #5ef2b2;
    --panel-left: #80f7a0;
    --panel-right: #fbff9f;
    --rust: #7a3a08;
    --neon: #33ff22;
    --teal: #1aa596;
    --ink: #151515;
    --white: #ffffff;
    --photo-concrete: #b9ad92;
    --photo-shed: #8c8a78;
  }
  * { margin: 0; padding: 0; box-sizing: border-box; }
  html, body { width: 782px; height: 1200px; overflow: hidden; background: var(--olive); }
  .flyer {
    position: relative;
    width: 782px;
    height: 1200px;
    overflow: hidden;
    font-family: "Ubuntu", sans-serif;
    color: var(--ink);
  }
  .backdrop { position: absolute; inset: 0; }
  .brand {
    position: absolute;
    left: 0; width: 782px; top: 44px;
    text-align: center;
  }
  .brand-dot {
    display: block;
    width: 46px; height: 46px;
    margin: 0 auto 8px;
    border-radius: 50%;
    background: #2a2a10;
  }
  .brand-name {
    font-family: "Ubuntu", sans-serif;
    font-weight: 400;
    font-size: 22px;
    line-height: 1.15;
    letter-spacing: 1px;
    color: #241f05;
    text-transform: uppercase;
  }
  .section-title {
    position: absolute;
    font-weight: 300;
    color: var(--mint);
    white-space: nowrap;
    line-height: 1;
  }
  .section-copy {
    position: absolute;
    white-space: nowrap;
    font-weight: 400;
  }
  .copy-lg { font-size: 12.4px; line-height: 16.6px; }
  .copy-sm { font-size: 10.2px; line-height: 14.4px; }
  .footer-text {
    position: absolute;
    color: var(--white);
    white-space: nowrap;
    font-weight: 400;
  }
  .call-label { color: var(--mint); font-size: 20px; font-weight: 300; }
</style>
</head>
<body>
<main class="flyer">
  <svg class="backdrop" width="782" height="1200" viewBox="0 0 782 1200" xmlns="http://www.w3.org/2000/svg">
    <defs>
      <linearGradient id="bgMain" x1="0" y1="0" x2="1" y2="1">
        <stop offset="0" stop-color="#9c8a12"/>
        <stop offset="0.35" stop-color="#d4b004"/>
        <stop offset="0.55" stop-color="#e6cc00"/>
        <stop offset="0.8" stop-color="#a9cc00"/>
        <stop offset="1" stop-color="#3d6512"/>
      </linearGradient>
      <linearGradient id="topArc" x1="0" y1="0" x2="0" y2="1">
        <stop offset="0" stop-color="#6a5d06"/>
        <stop offset="1" stop-color="#a99a2a"/>
      </linearGradient>
      <linearGradient id="rightGlow" x1="0" y1="0" x2="1" y2="0">
        <stop offset="0" stop-color="#d7b400"/>
        <stop offset="1" stop-color="#ffdf00"/>
      </linearGradient>
      <linearGradient id="lowerGreen" x1="0" y1="0" x2="1" y2="1">
        <stop offset="0" stop-color="#a07a10"/>
        <stop offset="0.5" stop-color="#7c8a08"/>
        <stop offset="1" stop-color="#2f5a12"/>
      </linearGradient>
      <linearGradient id="panel" x1="0" y1="0" x2="1" y2="0">
        <stop offset="0" stop-color="#80f7a0"/>
        <stop offset="1" stop-color="#fbff9f"/>
      </linearGradient>
      <linearGradient id="tab" x1="0" y1="0" x2="1" y2="0">
        <stop offset="0" stop-color="#a86b38"/>
        <stop offset="1" stop-color="#8a7c06"/>
      </linearGradient>
      <linearGradient id="tabRight" x1="0" y1="0" x2="1" y2="0">
        <stop offset="0" stop-color="#8a6e08"/>
        <stop offset="1" stop-color="#9c8d10"/>
      </linearGradient>
      <radialGradient id="cornerGlow" cx="0" cy="1" r="0.8">
        <stop offset="0" stop-color="#fff6d8"/>
        <stop offset="1" stop-color="#ffcf40" stop-opacity="0"/>
      </radialGradient>
    </defs>

    <rect width="782" height="1200" fill="url(#bgMain)"/>
    <polygon points="520,75 782,75 782,540 680,540 560,300" fill="url(#rightGlow)"/>
    <path d="M0,0 H782 V60 H670 Q560,228 391,228 Q222,228 110,60 H0 Z" fill="url(#topArc)"/>
    <path d="M0,60 H200 L300,140 L0,140 Z" fill="#8a7a10" opacity="0.55"/>
    <path d="M0,206 H66 L130,270 H0 Z" fill="#c8b450" opacity="0.55"/>
    <path d="M0,880 H782 V1200 H0 Z" fill="url(#lowerGreen)"/>
    <polygon points="400,890 782,890 782,1020 540,1020" fill="#a9d600" opacity="0.7"/>
    <rect x="0" y="900" width="300" height="300" fill="url(#cornerGlow)"/>

    <!-- neon guide lines -->
    <g fill="none" stroke="var(--neon)">
      <path d="M0,96 H130 Q260,250 391,252 Q522,250 652,96 H782" stroke-width="1.4"/>
      <path d="M0,126 H120 Q250,280 391,282 Q532,280 662,126 H782" stroke-width="1"/>
      <path d="M0,144 H104 Q240,300 391,300 Q542,300 676,144 H782" stroke-width="0.6"/>
    </g>
    <g fill="none" stroke="#c9b21a" stroke-width="1" opacity="0.7">
      <path d="M0,560 L60,528 H760"/>
      <path d="M0,585 L80,552 H520"/>
      <path d="M0,610 L100,578 H480"/>
      <path d="M400,890 L540,1020 H782"/>
    </g>

    <!-- deep grooving -->
    <polygon points="0,293 300,293 318,348 0,348" fill="url(#tab)"/>
    <polygon points="300,293 306,293 324,348 318,348" fill="#f2f000"/>
    <polygon points="0,346 512,346 560,502 0,502" fill="var(--rust)"/>
    <polygon points="0,346 508,346 554,494 0,494" fill="url(#panel)"/>
    <polygon points="504,346 512,346 560,502 552,502" fill="#ffee00"/>

    <!-- mini grooving -->
    <polygon points="486,558 782,558 782,609 472,609" fill="url(#tabRight)"/>
    <polygon points="480,558 488,558 474,609 466,609" fill="#ffee00"/>
    <polygon points="132,606 782,606 782,710 92,710" fill="var(--rust)"/>
    <polygon points="140,610 782,610 782,700 100,700" fill="url(#panel)"/>
    <rect x="92" y="700" width="690" height="8" fill="#ffee00"/>

    <!-- deep groove on slats -->
    <polygon points="0,750 438,750 460,806 0,806" fill="url(#tab)"/>
    <polygon points="438,750 446,750 462,806 454,806" fill="#ffee00"/>
    <polygon points="0,803 332,803 378,880 0,880" fill="var(--rust)"/>
    <polygon points="0,803 326,803 370,874 0,874" fill="url(#panel)"/>

    <!-- sensor plate sinking -->
    <polygon points="346,1007 782,1007 782,1051 330,1051" fill="#6f7a10"/>
    <polygon points="338,1007 346,1007 330,1051 322,1051" fill="#c8d400"/>
    <polygon points="250,1051 782,1051 782,1103 230,1103" fill="var(--rust)"/>
    <polygon points="254,1053 782,1053 782,1098 238,1098" fill="#80f7a0"/>

    <!-- photo hexagons: deep grooving cluster -->
    <g stroke="var(--teal)" stroke-width="1.6">
      <polygon points="606,264 666,264 698,326 666,386 606,386 576,326" fill="var(--photo-concrete)" role="img" aria-label="Photo of freshly grooved concrete barn floor"/>
      <polygon points="690,318 752,318 780,380 752,440 690,440 660,380" fill="#8f8f80" role="img" aria-label="Photo of grooving machine working on a shed floor"/>
      <polygon points="598,376 660,376 690,434 660,492 598,492 568,434" fill="#a68850" role="img" aria-label="Photo of grooved floor inside a cattle shed"/>
      <polygon points="686,424 748,424 778,480 748,536 686,536 656,480" fill="#c4c0b4" role="img" aria-label="Photo of long grooved alley in a dairy barn"/>
    </g>
    <!-- slats photo -->
    <polygon points="558,768 674,768 730,867 674,966 558,966 502,867" fill="none" stroke="var(--teal)" stroke-width="2"/>
    <polygon points="566,780 666,780 716,867 666,954 566,954 516,867" fill="var(--photo-shed)" role="img" aria-label="Photo of grooving machine on slatted floor in an open cattle shed"/>
    <!-- sensor plate photo -->
    <polygon points="56,946 174,946 232,1050 174,1154 56,1154 0,1050" fill="none" stroke="var(--neon)" stroke-width="2"/>
    <polygon points="62,966 166,966 212,1050 166,1134 62,1134 18,1050" fill="#8a8478" role="img" aria-label="Photo of a sensor plate sunk into a groove below floor level"/>

    <!-- footer icons -->
    <g fill="var(--mint)">
      <path d="M680,1164 a7,7 0 0 1 7,7 c0,6 -7,13 -7,13 c0,0 -7,-7 -7,-13 a7,7 0 0 1 7,-7 z M680,1168 a3,3 0 1 0 0.01,0 z" fill-rule="evenodd"/>
      <rect x="696" y="1164" width="22" height="22" rx="5"/>
      <circle cx="737" cy="1175" r="11"/>
    </g>
  </svg>

  <header class="brand">
    <span class="brand-dot"></span>
    <div class="brand-name">Marwell<br>Herd Services</div>
  </header>

  <h2 class="section-title" style="left:6px; top:307px; font-size:36px;">DEEP GROOVING</h2>
  <div class="section-copy copy-lg" style="left:11px; top:360px;">
    Ideal for Safety &amp; Efficiency<br>
    Our hugely popular deep straight line grooving, long lasting, minimal hoof wear.<br>
    <br>
    Create safe and secure flooring, cows walk without hesitation<br>
    &nbsp;Achieve groove spacing for optimal hoof function, reduce hoof trauma<br>
    Ideal grooves to new concrete or surfaces with little to no pattern or previous grooving<br>
    Ideal groove pattern as promoted by The pasturewide programme
  </div>

  <h2 class="section-title" style="left:496px; top:566px; font-size:36px;">MINI GROOVING</h2>
  <div class="section-copy copy-sm" style="left:181px; top:633px;">
    Smaller dimensions Ideal option for heifer housing and high activity areas such as parlours and handling areas<br>
    An ideal solution for regaining traction on old previous grooving that has lost its traction without loosing stability<br>
    Plaining, smoothing down rough concrete with previous aggressive grooving or patterns to reduce hoof trauma &amp; wear
  </div>

  <h2 class="section-title" style="left:11px; top:762px; font-size:36px;">DEEP GROOVE ON SLATS</h2>
  <div class="section-copy copy-sm" style="left:18px; top:826px;">
    Smoothing down rough concrete with previous aggressive<br>
    grooving or patterns to reduce hoof trauma &amp; wear
  </div>

  <h2 class="section-title" style="left:360px; top:1012px; font-size:36px;">SENSOR PLATE SINKING</h2>
  <div class="section-copy copy-sm" style="left:265px; top:1068px;">
    Sinking sensor plates for automated machines below surface level preventing accidental damage &amp; wear
  </div>

  <div class="footer-text call-label" style="left:526px; top:1142px;">CALL US</div>
  <div class="footer-text" style="left:497px; top:1173px; font-size:14px;">+EXAMPLE NUMBER</div>
  <div class="footer-text" style="left:282px; top:1173px; font-size:14px;">WWW.YOURWEBSITE.COM</div>
  <div class="footer-text" style="left:666px; top:1134px; font-size:14px;">CONTACT US</div>
</main>
</body>
</html>
```